Harborline Dance USA's Moonslipper

Poster Design for a Full Length Ballet

HDT Center for Dance Education
& Harborline Dance USA

directed by Rex & Marilyn Sotherby
Nora Whitcombe Palk, Resident Choreographer

present
"Moonslipper"

May 16 & 17 2015
Pemberton Music Hall
555 - 718-3946
www.harborlinedance.example

The logos do not have to be present
Decorative font only in the word Moonslipper

Industry/Entity Type

Education

Font styles to use
Decorative

Colors
0493ce
3277b5
886aae

```html
<!DOCTYPE html>
<html lang="en">
<head>
<meta charset="utf-8">
<title>Moonslipper — Harborline Dance USA</title>
<link href="https://fonts.googleapis.com/css2?family=Great+Vibes&family=Lato:wght@400;700&display=swap" rel="stylesheet">
<style>
  :root {
    --backdrop: #e4e5e7;
    --poster: #000000;
    --ink: #ffffff;
    --sky-deep: #3277b5;
    --sky-bright: #0493ce;
    --sky-cloud: #dfeaf3;
    --gold-dark: #7a5a12;
    --gold: #c89a2c;
    --gold-light: #e8c65a;
  }
  html, body {
    margin: 0;
    width: 1200px;
    height: 1199px;
    overflow: hidden;
    background: var(--backdrop);
  }
  .poster {
    position: absolute;
    left: 231px;
    top: 30px;
    width: 738px;
    height: 1140px;
    background: var(--poster);
    color: var(--ink);
    font-family: "Lato", sans-serif;
    text-align: center;
  }
  .event-line {
    position: absolute;
    top: 50px;
    left: 0;
    right: 0;
    margin: 0;
    font-size: 19px;
    word-spacing: 1px;
  }
  .event-line .divider { margin: 0 14px; }
  .artwork-frame {
    position: absolute;
    left: 138px;
    top: 114px;
    width: 465px;
    height: 555px;
    background: linear-gradient(135deg, var(--gold-light), var(--gold) 40%, var(--gold-dark) 75%, var(--gold));
  }
  .artwork-sky {
    position: absolute;
    left: 51px;
    top: 52px;
    width: 364px;
    height: 450px;
    background: linear-gradient(180deg, var(--sky-deep) 0%, var(--sky-bright) 35%, #8fb6d8 65%, var(--sky-cloud) 100%);
  }
  .title {
    position: absolute;
    top: 700px;
    left: 0;
    right: 0;
    margin: 0;
    font-family: "Great Vibes", cursive;
    font-weight: 400;
    font-size: 112px;
    line-height: 1.1;
    background: linear-gradient(180deg, var(--sky-bright) 25%, #ffffff 85%);
    -webkit-background-clip: text;
    background-clip: text;
    color: transparent;
  }
  .flourish {
    position: absolute;
    left: 315px;
    top: 877px;
    width: 108px;
    height: 14px;
    background: linear-gradient(90deg, transparent, #bdbdbd 20%, #bdbdbd 80%, transparent);
    opacity: 0.5;
    border-radius: 7px;
  }
  .presented-label {
    position: absolute;
    top: 904px;
    left: 0;
    right: 0;
    margin: 0;
    font-size: 19px;
    font-weight: 400;
    letter-spacing: 4px;
  }
  .presenters, .credits {
    position: absolute;
    left: 0;
    right: 0;
    margin: 0;
    font-size: 15px;
    line-height: 20px;
  }
  .presenters { top: 943px; }
  .credits { top: 985px; }
  .credits strong { font-weight: 700; font-size: 16px; }
  .rule {
    position: absolute;
    left: 80px;
    top: 1081px;
    width: 577px;
    height: 2px;
    background: linear-gradient(90deg, transparent, #ffffff 15%, #ffffff 85%, transparent);
  }
  .contact {
    position: absolute;
    top: 1105px;
    left: 0;
    right: 0;
    margin: 0;
    font-size: 12px;
  }
  .contact .divider { margin: 0 9px; }
</style>
</head>
<body>
  <main class="poster">
    <p class="event-line">May 16 &amp; 17 2015<span class="divider">||</span>Pemberton Music Hall</p>

    <div class="artwork-frame" role="img" aria-label="Ornate gilded picture frame">
      <div class="artwork-sky" role="img" aria-label="Glass slipper floating in a blue cloudy sky"></div>
    </div>

    <h1 class="title">Moonslipper</h1>
    <div class="flourish" role="img" aria-label="Small decorative flourish"></div>

    <h2 class="presented-label">PRESENTED BY</h2>
    <p class="presenters">HDT Center for Dance Education &amp; Harborline Dance USA</p>

    <p class="credits">
      directed by<br>
      <strong>Rex &amp; Marilyn Sotherby</strong><br>
      Nora Whitcombe Palk, Resident Choreographer
    </p>

    <div class="rule"></div>
    <p class="contact">555 - 718-3946<span class="divider">||</span>www.harborlinedance.example</p>
  </main>
</body>
</html>
```